Criação de Cartao de Visita para Computador & Internet
" Nossos clientes fazem o outsorcing da TI para nós, assim cuidamos de todos os recursos se serviços de TI, também vendemos hardwares e softwares "

```html
<!DOCTYPE html>
<html lang="pt-BR">
<head>
<meta charset="UTF-8">
<title>Nexo TI – Cartão de Visita</title>
<link rel="stylesheet" href="https://fonts.googleapis.com/css2?family=Montserrat:wght@300;400;600;700&display=swap">
<style>
  :root{
    --blue-deep:#0d4f86;
    --blue-mid:#1670b3;
    --blue-bright:#2a9ad6;
    --blue-soft:#5cb8e6;
    --white:#ffffff;
    --paper:#f4f6f8;
    --stage:#e3e6ea;
    --ink-blue:#0f5c99;
  }
  *{box-sizing:border-box;margin:0;padding:0}
  html,body{width:1200px;height:1200px;overflow:hidden}
  body{background:var(--stage);font-family:"Montserrat",sans-serif;position:relative}

  .card{position:absolute;border-radius:22px;overflow:hidden;background:var(--paper);box-shadow:0 6px 18px rgba(0,0,0,.12)}
  .card__bg{position:absolute;inset:0;width:100%;height:100%}

  /* Front card */
  .card--front{left:90px;top:330px;width:460px;height:780px}
  .brand{position:absolute;left:0;right:0;top:90px;display:flex;align-items:center;justify-content:center;gap:24px}
  .brand__dot{width:110px;height:110px;border-radius:50%;background:var(--blue-mid)}
  .brand__name{font-weight:600;font-size:46px;color:var(--blue-mid);letter-spacing:1px}

  .person{position:absolute;left:150px;top:430px;color:var(--white)}
  .person__name{font-weight:300;font-size:34px;line-height:1.1}
  .person__role{font-weight:400;font-size:17px;margin-top:6px}
  .person__division{font-weight:700;font-size:15px;margin-top:4px;letter-spacing:.5px}

  .contacts{position:absolute;left:82px;top:560px;list-style:none;color:var(--white)}
  .contacts__item{display:flex;align-items:center;gap:14px;margin-bottom:14px;font-size:14px;font-weight:400;line-height:1.3}
  .contacts__icon{flex:0 0 28px;width:28px;height:28px;border-radius:50%;background:var(--white);display:flex;align-items:center;justify-content:center}
  .contacts__icon svg{width:16px;height:16px}

  /* Back card */
  .card--back{left:560px;top:90px;width:580px;height:360px}
  .division{position:absolute;color:var(--white)}
  .division--it{left:34px;top:34px;width:280px}
  .division--events{left:340px;top:110px;width:220px;color:var(--ink-blue)}
  .division__title{font-weight:700;font-size:17px;line-height:1.2}
  .division__subtitle{font-weight:600;font-size:13px;line-height:1.25;margin-top:2px}
  .division--events .division__title,.division--events .division__subtitle{text-align:right}
  .division__list{list-style:none;margin-top:14px}
  .division__list li{position:relative;padding-left:16px;font-size:12.5px;font-weight:400;line-height:1.3;margin-bottom:6px}
  .division__list li::before{content:"";position:absolute;left:0;top:6px;width:6px;height:6px;border-radius:50%;background:currentColor}
  .division--events .division__list li::before{background:var(--blue-bright)}
</style>
</head>
<body>

  <!-- Front -->
  <section class="card card--front" aria-label="Frente do cartão">
    <svg class="card__bg" viewBox="0 0 460 780" preserveAspectRatio="none" aria-hidden="true">
      <defs>
        <linearGradient id="frontBlue" x1="0" y1="0" x2="1" y2="1">
          <stop offset="0" stop-color="#1f86c8"/>
          <stop offset="1" stop-color="#0d4f86"/>
        </linearGradient>
      </defs>
      <rect width="460" height="780" fill="#f4f6f8"/>
      <path d="M0 330 C 120 300 200 400 460 330 L460 780 L0 780 Z" fill="#5cb8e6"/>
      <path d="M0 360 C 140 330 220 420 460 360 L460 780 L0 780 Z" fill="url(#frontBlue)"/>
      <path d="M0 420 C 60 380 110 400 130 470 L130 780 L0 780 Z" fill="#2a9ad6" opacity=".35"/>
      <circle cx="380" cy="700" r="160" fill="#ffffff" opacity=".05"/>
    </svg>

    <div class="brand">
      <span class="brand__dot" aria-hidden="true"></span>
      <span class="brand__name">Nexo TI</span>
    </div>

    <div class="person">
      <p class="person__name">Marina Tavares</p>
      <p class="person__role">Diretora Executiva</p>
      <p class="person__division">DIVISÃO DE EVENTOS</p>
    </div>

    <ul class="contacts">
      <li class="contacts__item">
        <span class="contacts__icon"><svg viewBox="0 0 16 16"><path d="M4 2l2 3-1.3 1.3a8 8 0 0 0 5 5L11 10l3 2-1.5 2.2C7 14 2 9 1.8 3.5Z" fill="#1670b3"/></svg></span>
        <span>(11) 4020-1150<br>(11) 98765-4321</span>
      </li>
      <li class="contacts__item">
        <span class="contacts__icon"><svg viewBox="0 0 16 16"><path d="M8 1a5 5 0 0 0-5 5c0 4 5 9 5 9s5-5 5-9a5 5 0 0 0-5-5Zm0 7a2 2 0 1 1 0-4 2 2 0 0 1 0 4Z" fill="#1670b3"/></svg></span>
        <span>Rua das Acácias, 210 – Centro<br>São Paulo – SP</span>
      </li>
      <li class="contacts__item">
        <span class="contacts__icon"><svg viewBox="0 0 16 16"><rect x="2" y="4" width="12" height="8" rx="1" fill="#1670b3"/><path d="M2.5 4.5 8 9l5.5-4.5" stroke="#fff" stroke-width="1.2" fill="none"/></svg></span>
        <span>marina.tavares@nexoti.com.br</span>
      </li>
      <li class="contacts__item">
        <span class="contacts__icon"><svg viewBox="0 0 16 16"><circle cx="8" cy="8" r="6" fill="none" stroke="#1670b3" stroke-width="1.4"/><path d="M2 8h12M8 2c-3 3-3 9 0 12M8 2c3 3 3 9 0 12" stroke="#1670b3" stroke-width="1.2" fill="none"/></svg></span>
        <span>www.nexoti.com.br</span>
      </li>
    </ul>
  </section>

  <!-- Back -->
  <section class="card card--back" aria-label="Verso do cartão">
    <svg class="card__bg" viewBox="0 0 580 360" preserveAspectRatio="none" aria-hidden="true">
      <defs>
        <linearGradient id="backBlue" x1="0" y1="0" x2="1" y2="1">
          <stop offset="0" stop-color="#2a9ad6"/>
          <stop offset="1" stop-color="#0d4f86"/>
        </linearGradient>
      </defs>
      <rect width="580" height="360" fill="#f4f6f8"/>
      <path d="M0 0 L360 0 C 300 90 300 180 320 240 C 340 300 300 340 260 360 L0 360 Z" fill="#5cb8e6"/>
      <path d="M0 0 L340 0 C 280 90 280 180 300 240 C 320 300 280 340 240 360 L0 360 Z" fill="url(#backBlue)"/>
      <path d="M0 360 C 80 260 200 260 300 300 L300 360 Z" fill="#ffffff" opacity=".07"/>
      <path d="M330 0 L580 0 L580 80 C 480 110 400 90 330 0 Z" fill="#1670b3"/>
    </svg>

    <div class="division division--it">
      <p class="division__title">Divisão de TI</p>
      <p class="division__subtitle">Soluções em Tecnologia da Informação</p>
      <ul class="division__list">
        <li>Administração e Suporte de TI (outsourcing)</li>
        <li>Consultoria e Venda de Hardware e Software</li>
        <li>Cloud Solutions</li>
        <li>Data Center e Projetos de TI</li>
        <li>Segurança e Proteção de Dados</li>
      </ul>
    </div>

    <div class="division division--events">
      <p class="division__title">Divisão de Eventos</p>
      <p class="division__subtitle">Soluções para Gestão Jurídica</p>
      <ul class="division__list">
        <li>Simpósios</li>
        <li>Seminários</li>
        <li>Congressos</li>
        <li>Cursos</li>
        <li>Workshop</li>
        <li>Networking</li>
        <li>Convenções Empresariais</li>
      </ul>
    </div>
  </section>

</body>
</html>
```